Women's Health Company needs business card

We need a business card for a USA based women's health care company. We use digital technology to enhance therapy prescribed by clinicians for their patients

```html
<!DOCTYPE html>
<html lang="en">
<head>
<meta charset="utf-8">
<title>Corvela Health – Business Card</title>
<link href="https://fonts.googleapis.com/css2?family=Lato:wght@400;700&display=swap" rel="stylesheet">
<style>
  :root {
    --stage: #3a3a3c;
    --purple: #8d54a0;
    --teal: #72bdb5;
    --white: #ffffff;
    --ink: #5a5a5a;
  }
  * { box-sizing: border-box; margin: 0; padding: 0; }
  html, body { width: 1200px; height: 689px; overflow: hidden; }
  body {
    background: var(--stage);
    font-family: "Lato", sans-serif;
    position: relative;
  }
  .card {
    position: absolute;
    top: 196px;
    width: 520px;
    height: 297px;
    overflow: hidden;
    box-shadow: 0 10px 30px rgba(0,0,0,0.35);
  }
  .card-front { left: 60px; background: var(--purple); }
  .card-back { left: 620px; background: var(--purple); }

  .front-wordmark {
    position: absolute;
    inset: 0;
    display: flex;
    align-items: center;
    justify-content: center;
    gap: 16px;
    color: var(--white);
    font-weight: 400;
    font-size: 54px;
    letter-spacing: 1px;
  }
  .wordmark-dot {
    width: 14px; height: 14px;
    border-radius: 50%;
    background: var(--white);
  }

  .back-shapes { position: absolute; inset: 0; }

  .back-wordmark {
    position: absolute;
    top: 44px;
    right: 34px;
    display: flex;
    align-items: center;
    gap: 8px;
    color: var(--teal);
    font-weight: 400;
    font-size: 30px;
    letter-spacing: 0.5px;
  }
  .back-wordmark .wordmark-dot { width: 8px; height: 8px; background: var(--teal); }

  .contact {
    position: absolute;
    left: 88px;
    top: 158px;
  }
  .contact-name {
    color: var(--teal);
    font-weight: 700;
    font-size: 19px;
    letter-spacing: 0.5px;
    text-transform: uppercase;
  }
  .contact-role {
    color: var(--purple);
    font-size: 13px;
    margin-top: 1px;
    margin-bottom: 8px;
  }
  .contact-list { list-style: none; }
  .contact-list li {
    display: flex;
    align-items: center;
    gap: 9px;
    color: var(--ink);
    font-size: 11.5px;
    line-height: 16px;
  }
  .contact-list svg { width: 10px; height: 10px; fill: var(--purple); flex: none; }
</style>
</head>
<body>

  <section class="card card-front" aria-label="Card front">
    <div class="front-wordmark">
      <span class="wordmark-dot"></span>
      <span>Corvela Health</span>
    </div>
  </section>

  <section class="card card-back" aria-label="Card back">
    <svg class="back-shapes" viewBox="0 0 520 297" preserveAspectRatio="none">
      <path d="M0 18 C120 8 200 70 300 92 C400 114 470 100 520 78 L520 297 L0 297 Z" fill="var(--white)"/>
      <path d="M22 22 C120 14 200 66 300 86 C390 104 450 96 500 82" fill="none" stroke="var(--teal)" stroke-width="4" stroke-linecap="round"/>
      <path d="M330 80 C400 92 460 86 512 66" fill="none" stroke="var(--purple)" stroke-width="2.5" stroke-linecap="round"/>
    </svg>

    <div class="back-wordmark">
      <span class="wordmark-dot"></span>
      <span>Corvela Health</span>
    </div>

    <div class="contact">
      <p class="contact-name">Daniel Reyes</p>
      <p class="contact-role">Founder &amp; CEO</p>
      <ul class="contact-list">
        <li><svg viewBox="0 0 10 10"><path d="M2 0.5 L3.6 2.6 L2.8 3.6 C3.4 5 4.8 6.4 6.2 7 L7.2 6.2 L9.5 7.8 L8.4 9.5 C4.5 9.2 0.8 5.5 0.5 1.6 Z"/></svg>(555) 214-3380</li>
        <li><svg viewBox="0 0 10 10"><path d="M2.5 0 H7.5 V10 H2.5 Z M3.5 1 V8 H6.5 V1 Z"/></svg>(555) 214-3381</li>
        <li><svg viewBox="0 0 10 10"><path d="M2.5 0.5 H7.5 V3 H9.5 V7.5 H7.5 V9.5 H2.5 V7.5 H0.5 V3 H2.5 Z M3.5 1.5 V3 H6.5 V1.5 Z M3.5 6 V8.5 H6.5 V6 Z"/></svg>(555) 214-3382</li>
        <li><svg viewBox="0 0 10 10"><path d="M0.5 2 H9.5 V8 H0.5 Z M1.2 2.6 L5 5.4 L8.8 2.6"/></svg>info@corvelahealth.com</li>
        <li><svg viewBox="0 0 10 10"><circle cx="5" cy="5" r="4.5"/></svg>corvelahealth.com</li>
      </ul>
    </div>
  </section>

</body>
</html>
```